A landing page- for our luxury toothbrush company called "Vörn"

A landing page to gain interest, traction, and potentially presales for our luxury toothbrush brand Vörn. I would like something like this -- does not have to be exact
LANDING PAGE OUTLINE
1️⃣ HERO SECTION (Above the Fold)
Headline:
Rethink Your Daily Hollow.
Subheadline:
A luxury, refillable toothbrush designed with intention — where beauty meets dentistry.
Buttons:
Join the Founding List or Email list
Link to complete survey for 20% off first purchase
Small line underneath:
Launching Fall 2026 · Limited Keeper’s Edition
2️⃣ THE PROBLEM (Emotional Framing)
Headline:
Oral care hasn’t evolved like beauty has.
Copy:
We invest in skincare rituals.
We curate our bathrooms.
We obsess over packaging and detail.
Yet the toothbrush — something we use twice daily — remains clinical, disposable, and uninspired.
You deserve better.
3️⃣ THE PRODUCT (Your Differentiation)
Headline:
Designed to be Displayed. Engineered to Perform.
Bullets (Luxury + Function):
• Hand-finished premium prints on an acetate handle
• Slim sculptural silhouette
• Gold-accent detailing
• Replaceable brush head system
• Premium bristles (dentist-selected)
• Designed by a practicing dentist
- Custom engraving
4️⃣ THE REFILL MODEL
Headline:
Luxury That Lasts.
Instead of discarding your entire brush, simply replace the head every 3 months.
Cleaner. Smarter. Elevated.
Micro-copy:
Refill subscriptions available at launch.
5️⃣ SOCIAL IMPACT (Your 5% Donation Angle)
Headline:
Beauty With Purpose.
5% of profits are donated to organizations chosen by our community.
As a Founder, you help decide where we give.
6️⃣ SOCIAL PROOF (Even Pre-Launch)
You can use:
Dentist credibility statement
~not made yet- will edit in~
Example testimonial style:
“Finally, a toothbrush I don’t want to hide in a drawer.”
7️⃣ FOUNDER CTA SECTION
Headline:
Become a Founding Member.
Be the first to receive:
Early access pricing
Engraving perks
First charity vote
Follow us on:
Snapgrid
Clipreel
~ don't have these made yet, will add in later~
🎯 Design Direction
Page should feel closer to:
Plumette
Tovane
Hollow
Not:
Denta-K
Minimal navigation.
Lots of white space.
Cream, bone, tortoise, gold tones.
Soft serif typography.
I have attached a picture of the clean vibe I would like- doesn't have to be exact but for inspo
I will also include/add our mock up drawings when they are finished!
Thank you :)

```html
<!DOCTYPE html>
<html lang="en">
<head>
<meta charset="utf-8">
<title>Vörn — Rethink Your Daily Hollow</title>
<link rel="stylesheet" href="https://fonts.googleapis.com/css2?family=Playfair+Display:wght@400;500;600&family=Outfit:wght@300;400;500;600&display=swap">
<style>
:root{
  --cream:#fdf5e8;
  --bone:#fbf0dc;
  --gold:#e8c382;
  --ink:#0b0b0b;
  --text:#1c1c1c;
  --muted:#6b6457;
  --white:#ffffff;
  --serif:'Playfair Display', Georgia, serif;
  --sans:'Outfit', Helvetica, Arial, sans-serif;
}
*{box-sizing:border-box;margin:0;padding:0}
h1,h2,h3,blockquote{font-weight:400}
html,body{width:1200px;height:3565px;overflow:hidden;background:var(--cream);font-family:var(--sans);color:var(--text)}
.page{position:relative;width:1200px;height:3565px;overflow:hidden;background:var(--cream)}
.photo{position:absolute}

/* header */
.site-header{position:absolute;left:0;top:0;width:462px;height:62px;border-bottom:1px solid #eadcc2;background:var(--bone)}
.brand{position:absolute;left:111px;top:12px;font-family:var(--serif);font-size:28px;font-weight:400;color:var(--ink)}
.menu-toggle{position:absolute;left:306px;top:22px;width:32px;height:18px}
.menu-toggle span{display:block;height:1.5px;background:var(--ink);margin-bottom:6px}
.menu-toggle span:nth-child(2){width:24px}
.contact-btn{position:absolute;left:912px;top:28px;width:100px;height:33px;background:var(--white);font-size:8.5px;font-weight:600;letter-spacing:.3px;display:flex;align-items:center;justify-content:center;gap:5px;color:var(--ink)}

/* hero */
.hero-panel{position:absolute;left:0;top:62px;width:462px;height:535px;background:linear-gradient(135deg,#f7e7cc 0%,#fcf3e3 40%,#f3e0c0 75%,#f9ecd6 100%)}
.hero-photo{left:462px;top:0;width:738px;height:597px;background:linear-gradient(120deg,#6e5c4a 0%,#d9cfc4 35%,#e9e6e2 55%,#2b2f3d 75%,#c7c1ba 100%)}
.hero-title{position:absolute;left:113px;top:170px;font-family:var(--serif);font-size:52px;font-weight:600;line-height:1.03;color:var(--ink)}
.hero-sub{position:absolute;left:114px;top:288px;width:292px;font-size:11.5px;line-height:1.5;color:var(--text)}
.btn{position:absolute;width:244px;height:39px;display:flex;align-items:center;justify-content:center;gap:6px;font-size:10.5px;font-weight:600}
.btn-gold{background:var(--gold);color:var(--white)}
.btn-outline{border:1.3px solid var(--ink);color:var(--ink);background:transparent}
.hero-note{position:absolute;left:113px;top:445px;font-size:9.5px;color:var(--muted)}

/* problem */
.problem{position:absolute;left:0;top:597px;width:1200px;height:333px;background:var(--ink)}
.problem-photo{left:0;top:0;width:478px;height:333px;background:linear-gradient(110deg,#3a2a14 0%,#b08a3e 30%,#e9c986 50%,#c79a87 70%,#1a140c 100%)}
.problem-title{position:absolute;left:569px;top:92px;font-family:var(--serif);font-size:28px;color:var(--white)}
.problem-list{position:absolute;left:569px;top:144px;list-style:none}
.problem-list li{display:flex;align-items:center;gap:8px;font-size:10.5px;color:var(--white);height:22px}
.tick{width:10px;height:10px;border-radius:50%;background:var(--gold);display:inline-flex;align-items:center;justify-content:center}

/* features */
.features-title{position:absolute;left:112px;top:1040px;font-family:var(--serif);font-size:28px;color:var(--ink)}
.slider-btn{position:absolute;width:47px;height:47px;border-radius:50%;display:flex;align-items:center;justify-content:center}
.slider-btn.dark{background:var(--ink)}
.slider-btn.gold{background:var(--gold)}
.slider-btn.ghost{background:#2a2c36}
.card{position:absolute;top:1118px;width:281px;height:388px;background:var(--white)}
.card-title{position:absolute;left:22px;top:24px;font-family:var(--serif);font-size:15px;line-height:1.35;color:var(--ink)}
.card-photo{left:22px;top:87px;width:235px;height:251px}
.card-arrow{position:absolute;left:22px;top:356px}

/* refill + purpose */
.split-title{position:absolute;font-family:var(--serif);font-size:29px;color:var(--ink)}
.split-copy{position:absolute;font-size:11px;line-height:1.55;color:var(--text)}
.split-strong{position:absolute;font-size:15px;font-weight:500;color:var(--ink)}
.split-micro{position:absolute;font-size:8.5px;color:var(--muted)}

/* testimonials */
.testimonials{position:absolute;left:0;top:2423px;width:1200px;height:431px;background:linear-gradient(135deg,#0b0d16 0%,#161a29 50%,#0a0c14 100%);overflow:hidden}
.center{position:absolute;left:0;width:1200px;text-align:center;color:var(--white)}
.t-title{top:78px;font-family:var(--serif);font-size:28px;line-height:1.2}
.t-sub{top:126px;font-size:11.5px}
.t-rule{position:absolute;left:291px;top:175px;width:620px;height:1px;background:#3a3d4d}
.t-quote{top:204px;font-family:var(--serif);font-size:28px;line-height:1.15}

/* founding */
.found-title{position:absolute;left:188px;top:2985px;font-family:var(--serif);font-size:29px;color:var(--ink)}
.found-sub{position:absolute;left:188px;top:3028px;font-size:10.5px;color:var(--text)}
.perk{position:absolute;top:2991px;width:140px;text-align:center}
.perk-box{margin:0 auto;width:102px;height:102px;background:var(--bone);display:flex;align-items:center;justify-content:center}
.perk-label{margin-top:20px;font-family:var(--serif);font-size:13px;color:var(--ink)}

/* footer */
.footer{position:absolute;left:0;top:3261px;width:1200px;height:304px;background:var(--cream);border-top:4px solid #f1e2c6}
.footer-brand{position:absolute;left:108px;top:44px;font-family:var(--serif);font-size:118px;font-weight:400;line-height:1;color:var(--ink)}
.social{position:absolute;top:100px;display:flex;align-items:center;gap:8px;font-size:12px;color:var(--ink)}
.social-dot{width:36px;height:36px;border-radius:50%;background:var(--ink)}
.footer-link{position:absolute;top:113px;font-size:12px;color:var(--ink)}
.footer-rule{position:absolute;left:111px;top:247px;width:977px;height:1px;background:#d8ccb6}
.copyright{position:absolute;left:0;width:1200px;top:269px;text-align:center;font-size:11px;color:var(--ink)}
.to-top{position:absolute;left:1125px;top:218px;width:36px;height:36px;border-radius:50%;background:var(--ink);display:flex;align-items:center;justify-content:center}
</style>
</head>
<body>
<div class="page">

  <div class="hero-panel" role="img" aria-label="Cream and gold marbled paper texture"></div>
  <div class="photo hero-photo" role="img" aria-label="Navy electric toothbrush on a charging tray with spare heads and a travel case on a marble bathroom counter"></div>
  <header class="site-header">
    <div class="brand">Vörn</div>
    <div class="menu-toggle"><span></span><span></span><span></span></div>
  </header>
  <a class="contact-btn">CONTACT US
    <svg width="8" height="8" viewBox="0 0 8 8"><path d="M1 7L7 1M2.5 1H7V5.5" stroke="#0b0b0b" stroke-width="1" fill="none"/></svg></a>

  <h1 class="hero-title">Rethink Your<br>Daily Hollow.</h1>
  <p class="hero-sub">A luxury, refillable toothbrush designed with intention where beauty meets dentistry.</p>
  <a class="btn btn-gold" style="left:113px;top:338px">Join the Founding List
    <svg width="8" height="8" viewBox="0 0 8 8"><path d="M1 7L7 1M2.5 1H7V5.5" stroke="#fff" stroke-width="1" fill="none"/></svg></a>
  <a class="btn btn-outline" style="left:113px;top:386px">Complete Survey for 20% Off
    <svg width="8" height="8" viewBox="0 0 8 8"><path d="M1 7L7 1M2.5 1H7V5.5" stroke="#0b0b0b" stroke-width="1" fill="none"/></svg></a>
  <p class="hero-note">Launching Fall 2026 · Limited Keeper’s Edition</p>

  <section class="problem">
    <div class="photo problem-photo" role="img" aria-label="Smiling woman with curly hair in front of gold brushstrokes"></div>
    <h2 class="problem-title">Oral care hasn’t evolved like beauty has.</h2>
    <ul class="problem-list">
      <li><span class="tick"><svg width="6" height="6" viewBox="0 0 6 6"><path d="M1 3l1.4 1.4L5 1.6" stroke="#0b0b0b" stroke-width="1" fill="none"/></svg></span>We invest in skincare rituals.</li>
      <li><span class="tick"><svg width="6" height="6" viewBox="0 0 6 6"><path d="M1 3l1.4 1.4L5 1.6" stroke="#0b0b0b" stroke-width="1" fill="none"/></svg></span>We curate our bathrooms.</li>
      <li><span class="tick"><svg width="6" height="6" viewBox="0 0 6 6"><path d="M1 3l1.4 1.4L5 1.6" stroke="#0b0b0b" stroke-width="1" fill="none"/></svg></span>We obsess over packaging and detail.</li>
      <li><span class="tick"><svg width="6" height="6" viewBox="0 0 6 6"><path d="M1 3l1.4 1.4L5 1.6" stroke="#0b0b0b" stroke-width="1" fill="none"/></svg></span>Yet the toothbrush — something we use twice daily — remains clinical, disposable, and uninspired.</li>
      <li><span class="tick"><svg width="6" height="6" viewBox="0 0 6 6"><path d="M1 3l1.4 1.4L5 1.6" stroke="#0b0b0b" stroke-width="1" fill="none"/></svg></span>You deserve better.</li>
    </ul>
  </section>

  <h2 class="features-title">Designed to be Displayed. Engineered to Perform.</h2>
  <a class="slider-btn dark" style="left:987px;top:1036px"><svg width="14" height="10" viewBox="0 0 14 10"><path d="M13 5H1M5 1L1 5l4 4" stroke="#fff" stroke-width="1.2" fill="none"/></svg></a>
  <a class="slider-btn gold" style="left:1040px;top:1036px"><svg width="14" height="10" viewBox="0 0 14 10"><path d="M1 5h12M9 1l4 4-4 4" stroke="#fff" stroke-width="1.2" fill="none"/></svg></a>

  <article class="card" style="left:112px">
    <h3 class="card-title">Hand-finished premium prints<br>on an acetate handle</h3>
    <div class="photo card-photo" role="img" aria-label="Woman in glasses brushing her teeth" style="background:linear-gradient(135deg,#e8e4df,#c9b9a7 60%,#8e8b86)"></div>
    <svg class="card-arrow" width="26" height="14" viewBox="0 0 26 14"><path d="M1 7h23M18 1l6 6-6 6" stroke="#0b0b0b" stroke-width="1.2" fill="none"/></svg>
  </article>
  <article class="card" style="left:418px">
    <h3 class="card-title">Slim sculptural<br>silhouette</h3>
    <div class="photo card-photo" role="img" aria-label="Stone toothbrush holder and soap dispenser on a shelf" style="background:linear-gradient(135deg,#9b978f,#cfc6b8 55%,#e6e1da)"></div>
    <svg class="card-arrow" width="26" height="14" viewBox="0 0 26 14"><path d="M1 7h23M18 1l6 6-6 6" stroke="#0b0b0b" stroke-width="1.2" fill="none"/></svg>
  </article>
  <article class="card" style="left:725px">
    <h3 class="card-title">Gold-accent<br>detailing</h3>
    <div class="photo card-photo" role="img" aria-label="Gold faucet against warm wood paneling" style="background:linear-gradient(120deg,#2d2a28 0%,#efece7 35%,#b98a52 70%,#8a5a2c)"></div>
    <svg class="card-arrow" width="26" height="14" viewBox="0 0 26 14"><path d="M1 7h23M18 1l6 6-6 6" stroke="#0b0b0b" stroke-width="1.2" fill="none"/></svg>
  </article>
  <article class="card" style="left:1032px">
    <h3 class="card-title">Replaceable brush<br>head system</h3>
    <div class="photo card-photo" role="img" aria-label="Hand holding a replacement brush head" style="background:linear-gradient(135deg,#eef0f1,#e9cbb8 60%,#f3f3f3)"></div>
    <svg class="card-arrow" width="26" height="14" viewBox="0 0 26 14"><path d="M1 7h23M18 1l6 6-6 6" stroke="#0b0b0b" stroke-width="1.2" fill="none"/></svg>
  </article>

  <h2 class="split-title" style="left:227px;top:1710px">Luxury That Lasts.</h2>
  <p class="split-copy" style="left:229px;top:1757px;width:280px">Instead of discarding your entire brush, simply replace the head every 3 months.</p>
  <p class="split-strong" style="left:229px;top:1806px">Cleaner. Smarter. Elevated.</p>
  <p class="split-micro" style="left:228px;top:1842px">Refill subscriptions available at launch.</p>
  <div class="photo" role="img" aria-label="Two gold toothbrushes with white and grey bristles resting on blush silk" style="left:599px;top:1612px;width:489px;height:353px;background:linear-gradient(135deg,#caa78d 0%,#e6cbb8 40%,#c6a27d 70%,#efe2d6 100%)"></div>

  <div class="photo" role="img" aria-label="Woman with red hair brushing her teeth at a bathroom mirror" style="left:112px;top:1965px;width:487px;height:355px;background:linear-gradient(120deg,#e9e3dc 0%,#c9773f 35%,#d8d4d0 60%,#b59b76 100%)"></div>
  <h2 class="split-title" style="left:714px;top:2085px">Beauty With Purpose.</h2>
  <p class="split-copy" style="left:716px;top:2130px;width:250px">5% of profits are donated to organizations chosen by our community.</p>
  <p class="split-copy" style="left:716px;top:2179px">As a Founder, you help decide where we give.</p>

  <section class="testimonials" role="img" aria-label="Dark navy background with soft gold light">
    <h2 class="center t-title">What Early Supporters Are Saying</h2>
    <p class="center t-sub">Dentist credibility statement (To be added)</p>
    <div class="t-rule"></div>
    <blockquote class="center t-quote">“Finally, a toothbrush I don’t want<br>to hide in a drawer.”</blockquote>
    <a class="slider-btn ghost" style="left:550px;top:315px"><svg width="14" height="10" viewBox="0 0 14 10"><path d="M13 5H1M5 1L1 5l4 4" stroke="#fff" stroke-width="1.2" fill="none"/></svg></a>
    <a class="slider-btn gold" style="left:603px;top:315px"><svg width="14" height="10" viewBox="0 0 14 10"><path d="M1 5h12M9 1l4 4-4 4" stroke="#fff" stroke-width="1.2" fill="none"/></svg></a>
  </section>

  <h2 class="found-title">Become a Founding Member.</h2>
  <p class="found-sub">Be the first to receive:</p>
  <a class="btn btn-gold" style="left:191px;top:3060px">Join the Founding List
    <svg width="8" height="8" viewBox="0 0 8 8"><path d="M1 7L7 1M2.5 1H7V5.5" stroke="#fff" stroke-width="1" fill="none"/></svg></a>
  <a class="btn btn-outline" style="left:191px;top:3108px">Complete Survey for 20% Off
    <svg width="8" height="8" viewBox="0 0 8 8"><path d="M1 7L7 1M2.5 1H7V5.5" stroke="#0b0b0b" stroke-width="1" fill="none"/></svg></a>

  <div class="perk" style="left:615px">
    <div class="perk-box"><svg width="42" height="44" viewBox="0 0 42 44" fill="none" stroke="#0b0b0b" stroke-width="1.4"><circle cx="21" cy="17" r="14"/><circle cx="21" cy="17" r="8"/><path d="M13 29l-4 12 6-3 3 5 3-10M29 29l4 12-6-3-3 5-3-10"/></svg></div>
    <p class="perk-label">Early access pricing</p>
  </div>
  <div class="perk" style="left:752px">
    <div class="perk-box"><svg width="46" height="42" viewBox="0 0 46 42" fill="none" stroke="#0b0b0b" stroke-width="1.4"><circle cx="15" cy="5" r="3"/><circle cx="23" cy="5" r="3"/><circle cx="31" cy="5" r="3"/><path d="M6 16v14l8 8h6V28l-8-8M40 16v14l-8 8h-6V28l8-8M17 22c0-4 6-5 6 0 0-5 6-4 6 0s-6 8-6 8-6-4-6-8z"/></svg></div>
    <p class="perk-label">Engraving perks</p>
  </div>
  <div class="perk" style="left:889px">
    <div class="perk-box"><svg width="42" height="42" viewBox="0 0 42 42" fill="none" stroke="#0b0b0b" stroke-width="1.4"><rect x="4" y="22" width="34" height="16"/><path d="M4 22l6-8h22l6 8M14 22V6h12l4 4v12M18 12h8M18 16h8"/></svg></div>
    <p class="perk-label">First charity vote</p>
  </div>

  <footer class="footer">
    <div class="footer-brand">Vörn</div>
    <div class="social" style="left:498px"><span class="social-dot"></span>Clipreel</div>
    <div class="social" style="left:603px"><span class="social-dot"></span>Snapgrid</div>
    <a class="footer-link" style="left:886px">Terms &amp; Condition</a>
    <a class="footer-link" style="left:1012px">Privacy Policy</a>
    <a class="to-top"><svg width="10" height="12" viewBox="0 0 10 12"><path d="M5 11V1M1 5l4-4 4 4" stroke="#fff" stroke-width="1.2" fill="none"/></svg></a>
    <div class="footer-rule"></div>
    <p class="copyright">© Copyright 2026 Vörn, All Rights Reserved</p>
  </footer>

</div>
</body>
</html>
```